Website design for KOVIL – data platform for healthcare & social housing

We’re looking for a clean, modern multi-page website design for KOVIL — a data platform for healthcare and social housing.

📎 Please read the attached PDF for full structure, context, and design guidance.
The briefing is essential to understanding this project.

➡️ For the initial submission, only the homepage design (including header and footer) is required.

This will help us assess design direction and fit.

The full project includes four levels (homepage, general page, product overview, and product detail), which will be completed after selecting the final designer.

Industry/Entity Type

data platform for healthcare & social housing

Number of Pages Required

1 page

Font styles to use
Sans Serif

Requirements
Must have
• Please read the attached PDF
Nice to have
Should not have

```html
<!DOCTYPE html>
<html lang="en">
<head>
<meta charset="utf-8">
<title>KOVIL – Data platform for healthcare &amp; social housing</title>
<link href="https://fonts.googleapis.com/css2?family=Exo+2:wght@500;600;700&family=Roboto:wght@400;500;700&display=swap" rel="stylesheet">
<style>
:root{
  --navy:#123e7c;
  --navy-dark:#0f3f80;
  --orange:#f57c14;
  --teal:#29a9bd;
  --sky:#7dd8e8;
  --sky-soft:#eef8fc;
  --ink:#222a33;
  --muted:#55606b;
  --white:#ffffff;
}
*{margin:0;padding:0;box-sizing:border-box}
html,body{width:1200px;height:3752px;overflow:hidden}
body{position:relative;background:var(--white);font-family:"Roboto",Arial,sans-serif;color:var(--ink)}
.abs{position:absolute}
h1,h2,h3,.heading{font-family:"Exo 2","Roboto",sans-serif;font-weight:700;letter-spacing:.5px}
.btn{position:absolute;display:flex;align-items:center;justify-content:space-between;height:40px;padding:0 16px;font-size:12px;font-weight:700;letter-spacing:.4px;color:var(--white);text-transform:uppercase;white-space:nowrap;text-decoration:none}
.btn::after{content:"";flex:none;width:6px;height:6px;border-radius:50%;background:currentColor;margin-left:12px}
.btn-orange{background:var(--orange)}
.btn-navy{background:var(--navy)}
.btn-teal{background:var(--teal)}
.btn-white{background:var(--white);color:var(--navy)}
.btn-white::after{background:var(--navy)}
.title-rule{display:flex;align-items:center;justify-content:center;gap:10px;font-size:31px;color:var(--ink);white-space:nowrap}
.title-rule .rule{position:relative;width:58px;height:2px;background:var(--orange)}
.title-rule .rule::before{content:"";position:absolute;left:-3px;top:-2px;width:6px;height:6px;border-radius:50%;background:var(--orange)}
.title-rule .rule.r::before{left:auto;right:-3px}

/* header */
.site-header{left:0;top:0;width:1200px;height:56px;background:var(--white);border-top:3px solid var(--orange)}
.brand{font-family:"Exo 2",sans-serif;font-weight:700;font-size:28px;letter-spacing:5px;color:var(--navy)}
.main-nav{left:314px;top:22px;display:flex;gap:17px;font-size:11px;font-weight:700;color:var(--navy);white-space:nowrap}

/* hero */
.hero-media{left:0;top:56px;width:1200px;height:585px;background:linear-gradient(100deg,#8fb7cd 0%,#b7d3e2 35%,#d6e6ef 60%,#c7d8e2 100%)}
.hero-title{left:122px;top:222px;font-size:44px;line-height:53px;color:var(--white);font-weight:600}
.hero-sub{left:122px;top:391px;font-size:15px;color:var(--white)}

/* what is */
.what-media{left:122px;top:684px;width:460px;height:316px;border-radius:6px;background:linear-gradient(135deg,#cfd8e0 0%,#e8ddd2 50%,#b9cbd8 100%)}
.what-title{left:651px;top:688px;font-size:29px;display:flex;align-items:center;gap:10px;white-space:nowrap}
.what-title .rule{width:56px;height:2px;background:var(--orange);position:relative}
.what-title .rule::after{content:"";position:absolute;right:-2px;top:-2px;width:6px;height:6px;border-radius:50%;background:var(--orange)}
.what-copy{left:651px;top:733px;width:340px;font-size:11px;line-height:17px;color:var(--muted)}
.what-copy p+p{margin-top:16px}
.sector{display:flex;align-items:center;gap:8px;font-size:12.5px;font-weight:700;color:var(--navy);white-space:nowrap}
.sector .dot{width:42px;height:42px;border-radius:50%;background:var(--teal);display:flex;align-items:center;justify-content:center}

/* helps */
.helps-band{left:0;top:1172px;width:1200px;height:128px;background:var(--sky)}
.helps-shape{left:204px;top:1085px;width:792px;height:298px;border-radius:150px;background:var(--sky)}
.help-circle{width:206px;height:206px;border-radius:50%;background:var(--white);border:5px solid var(--white);box-shadow:inset 0 0 0 2px var(--sky);display:flex;flex-direction:column;align-items:center;justify-content:flex-start;padding-top:30px;font-family:"Exo 2",sans-serif;font-weight:700;font-size:16px;color:var(--ink);text-align:center;line-height:19px}
.help-circle .stem{width:2px;height:18px;background:var(--orange);position:relative;margin:4px 0 16px}
.help-circle .stem::after{content:"";position:absolute;left:-2px;bottom:-3px;width:6px;height:6px;border-radius:50%;background:var(--orange)}
.helps-notch{left:480px;top:1366px;width:240px;height:40px;border-radius:40px 40px 0 0;background:var(--white)}

/* products */
.products{left:0;top:1488px;width:1200px;height:555px;background:var(--sky-soft)}
.prod-card{top:1661px;width:224px;height:259px;border-radius:4px;overflow:hidden;display:flex;align-items:flex-end;justify-content:center;padding-bottom:20px;font-family:"Exo 2",sans-serif;font-weight:700;font-size:15px;color:var(--white);letter-spacing:.4px;white-space:nowrap}
.prod-icon{top:1642px;width:40px;height:40px;border-radius:50%;background:var(--teal);border:3px solid var(--white);display:flex;align-items:center;justify-content:center}

/* audience */
.aud-circle{top:2155px;width:201px;height:201px;border-radius:50%;background:var(--white);border:1.5px solid #8fc7e0;box-shadow:0 6px 0 -1px var(--sky);display:flex;flex-direction:column;align-items:center;padding-top:34px;font-family:"Exo 2",sans-serif;font-weight:700;font-size:15.5px;color:var(--ink);text-align:center;line-height:18px}
.aud-circle .stem{width:2px;height:16px;background:var(--orange);position:relative;margin:2px 0 14px}
.aud-circle .stem::after{content:"";position:absolute;left:-2px;bottom:-3px;width:6px;height:6px;border-radius:50%;background:var(--orange)}

/* community */
.community-media{left:0;top:2426px;width:1200px;height:402px;background:linear-gradient(90deg,#c9a48f 0%,#e1c7b7 30%,#f3e7de 55%,#fbeee3 75%,#fbd3a5 100%)}
.community-title{left:687px;top:2532px;font-size:29px;white-space:nowrap}
.community-copy{left:687px;top:2574px;width:370px;font-size:11px;line-height:17px;color:var(--muted)}
.community-copy p+p{margin-top:16px}

/* testimonials */
.clients-bg{left:0;top:2828px;width:1200px;height:401px;background:linear-gradient(180deg,#ffffff 0%,#f4fafd 60%,#e3f3fa 100%)}
.quote-card{top:2941px;width:406px;height:230px;background:var(--white);border:1.5px solid #9fb9d8;border-radius:3px;padding:34px 32px}
.quote-head{display:flex;align-items:center;gap:14px}
.avatar{width:50px;height:50px;border-radius:50%;background:linear-gradient(135deg,#f0c7a8,#c98f6c);border:3px solid var(--teal)}
.quote-name{font-size:12px;font-weight:700;color:var(--ink);margin-bottom:4px}
.stars{display:flex;gap:2px}
.quote-mark{position:absolute;right:22px;top:4px;font-family:Georgia,serif;font-size:110px;color:#e2e4e7;line-height:1}
.quote-text{margin-top:22px;font-size:11px;line-height:17.5px;color:var(--muted)}
.arrow-btn{top:3032px;width:24px;height:24px;border-radius:50%;border:1.5px solid var(--teal);display:flex;align-items:center;justify-content:center}

/* cta */
.cta{left:0;top:3229px;width:1200px;height:276px;background:var(--teal)}
.cta-title{left:0;top:3316px;width:1200px;color:var(--white)}
.cta-title .rule,.cta-title .rule::before{background:var(--white)}
.cta-sub{left:0;top:3363px;width:1200px;text-align:center;font-size:13px;color:var(--white)}

/* footer */
.site-footer{left:0;top:3505px;width:1200px;height:247px;background:var(--navy-dark);color:var(--white)}
.foot-col h4{font-family:"Exo 2",sans-serif;font-size:14px;letter-spacing:1px;margin-bottom:16px}
.foot-divider{top:3535px;width:1px;height:185px;background:rgba(255,255,255,.35)}
.foot-small{font-size:8.5px;line-height:16px}
.contact-row{display:flex;align-items:center;gap:10px;font-size:8.5px;margin-bottom:10px}
.contact-row .ic{width:26px;height:26px;border-radius:50%;border:1.5px solid var(--white);display:flex;align-items:center;justify-content:center}
.foot-links{font-size:9px;line-height:19px}
</style>
</head>
<body>

<header class="site-header abs">
  <div class="brand abs" style="left:122px;top:8px">KOVIL</div>
  <nav class="main-nav abs">
    <span>WHAT IS KOVIL?</span><span>PRODUCTS</span><span>WHO IT'S FOR</span><span>COMMUNITY</span><span>ABOUT US</span><span>CONTACT</span>
  </nav>
  <a class="btn btn-teal" style="left:840px;top:10px;height:33px;width:122px;font-size:11px;padding:0 14px">Plan a demo</a>
  <a class="btn btn-orange" style="left:967px;top:10px;height:33px;width:111px;font-size:11px;padding:0 14px">Start KOVIL</a>
</header>

<section class="hero">
  <div class="hero-media abs" role="img" aria-label="Healthcare professional in a lab coat holding a tablet showing data charts in a bright clinic"></div>
  <h1 class="hero-title abs">MORE IMPACT WITH<br>BETTER CONTROL<br>OVER DATA</h1>
  <p class="hero-sub abs">Data analytics for Healthcare and Social Housing</p>
  <a class="btn btn-orange" style="left:122px;top:432px;width:139px">Products</a>
  <a class="btn btn-navy" style="left:269px;top:432px;width:139px">Plan a demo</a>
</section>

<section class="what">
  <div class="what-media abs" role="img" aria-label="Photo collage of people working with data dashboards on a laptop"></div>
  <h2 class="what-title abs">WHAT IS KOVIL? <span class="rule"></span></h2>
  <div class="what-copy abs">
    <p>KOVIL is a Data analytics Platform for the Healthcare sector and social housing sector. We centralize, analyze, and visualize the data that matters — turning insight into action.</p>
    <p>Whether you're tackling homelessness, hospital discharge delays, or housing quality, KOVIL gives you the tools to understand the full picture and respond with confidence.</p>
  </div>
  <div class="sector abs" style="left:651px;top:869px">
    <span class="dot"><svg width="24" height="22" viewBox="0 0 24 22" fill="none" stroke="#fff" stroke-width="1.6"><path d="M12 20S2 13.5 2 7a5 5 0 0 1 10-1 5 5 0 0 1 10 1c0 6.5-10 13-10 13z"/><path d="M4 10h4l2-3 3 6 2-3h5"/></svg></span>Healthcare Sector
  </div>
  <div class="sector abs" style="left:829px;top:869px">
    <span class="dot"><svg width="22" height="22" viewBox="0 0 22 22" fill="none" stroke="#fff" stroke-width="1.6"><path d="M3 10l8-7 8 7v9H3z"/><path d="M9 19v-5h4v5"/></svg></span>Social Housing Sector
  </div>
  <a class="btn btn-orange" style="left:651px;top:938px;width:159px">What is KOVIL?</a>
</section>

<section class="helps">
  <h2 class="title-rule abs" style="left:0;top:1048px;width:1200px"><span class="rule"></span>HOW KOVIL HELPS<span class="rule r"></span></h2>
  <div class="helps-band abs"></div>
  <div class="helps-shape abs"></div>
  <div class="help-circle abs" style="left:230px;top:1130px">
    <svg width="64" height="64" viewBox="0 0 64 64" fill="none" stroke="#123e7c" stroke-width="2.5"><path d="M32 6l26 14-26 14L6 20z"/><path d="M6 30l26 14 26-14"/><path d="M6 40l26 14 26-14"/><path d="M20 20l12-6 12 6-12 6z"/></svg>
    <span class="stem"></span>PLATFORM AND<br>PRODUCTS
  </div>
  <div class="help-circle abs" style="left:494px;top:1130px">
    <svg width="66" height="64" viewBox="0 0 66 64" fill="none" stroke="#123e7c" stroke-width="2.5"><path d="M33 58S4 40 4 20A14 14 0 0 1 33 12a14 14 0 0 1 29 8c0 20-29 38-29 38z"/><circle cx="23" cy="24" r="5"/><circle cx="43" cy="24" r="5"/><circle cx="33" cy="35" r="5"/><path d="M16 38a7 7 0 0 1 14 0M36 38a7 7 0 0 1 14 0"/></svg>
    <span class="stem"></span>COMMUNITY
  </div>
  <div class="help-circle abs" style="left:762px;top:1130px">
    <svg width="64" height="64" viewBox="0 0 64 64" fill="none" stroke="#123e7c" stroke-width="2.5"><path d="M32 4l5 6 7-2 2 7 7 2-2 7 6 5-6 5 2 7-7 2-2 7-7-2-5 6-5-6-7 2-2-7-7-2 2-7-6-5 6-5-2-7 7-2 2-7 7 2z"/><circle cx="32" cy="32" r="14"/><circle cx="32" cy="26" r="4"/><path d="M32 30v12M27 36h10"/></svg>
    <span class="stem"></span>BI-AS-A-SERVICE
  </div>
  <div class="helps-notch abs"></div>
  <a class="btn btn-orange" style="left:535px;top:1379px;width:130px">More info</a>
</section>

<section>
  <div class="products abs"></div>
  <h2 class="heading abs" style="left:0;top:1536px;width:1200px;text-align:center;font-size:31px">PRODUCTS OVERVIEW</h2>
  <svg class="abs" style="left:230px;top:1582px" width="742" height="64" viewBox="0 0 742 64" fill="none" stroke="#9fc4dc" stroke-width="1.5"><path d="M3 62V10a8 8 0 0 1 8-8h720a8 8 0 0 1 8 8v52M247 2v60M491 2v60"/></svg>
  <div class="prod-card abs" role="img" aria-label="Woman with a lanyard viewing data screens" style="left:122px;background:linear-gradient(160deg,#1d3550,#7e6b65 55%,#2c3c56)">PUBLIC DATA ACCESS</div>
  <div class="prod-card abs" role="img" aria-label="Analyst on the phone in front of a monitor with market charts" style="left:366px;background:linear-gradient(160deg,#2b3a4c,#586c82 50%,#a7b1bd)">CLIMATE RISK SCAN</div>
  <div class="prod-card abs" role="img" aria-label="Coin stacks balanced on a seesaw with a green ball" style="left:609px;background:linear-gradient(180deg,#b79880,#ddd4c8 45%,#a9bcb2)">PRICING BENCHMARK</div>
  <div class="prod-card abs" role="img" aria-label="Hands reviewing coins and financial reports on a desk" style="left:853px;background:linear-gradient(160deg,#3c4b63,#a0a7ae 55%,#b8c3cc)">COST MODEL</div>
  <div class="prod-icon abs" style="left:212px"><svg width="20" height="20" viewBox="0 0 20 20" fill="none" stroke="#fff" stroke-width="1.5"><circle cx="10" cy="6" r="3"/><path d="M4 18v-3a6 6 0 0 1 12 0v3M10 11v7"/></svg></div>
  <div class="prod-icon abs" style="left:457px"><svg width="20" height="20" viewBox="0 0 20 20" fill="none" stroke="#fff" stroke-width="1.5"><circle cx="8" cy="8" r="5"/><path d="M12 12l5 5M6 8h4M8 6v4"/></svg></div>
  <div class="prod-icon abs" style="left:701px"><svg width="20" height="20" viewBox="0 0 20 20" fill="none" stroke="#fff" stroke-width="1.5"><path d="M3 17h14M5 15v-4M9 15V8M13 15V5M3 9l5-4 4 2 5-4"/></svg></div>
  <div class="prod-icon abs" style="left:945px"><svg width="20" height="20" viewBox="0 0 20 20" fill="none" stroke="#fff" stroke-width="1.5"><rect x="3" y="4" width="14" height="13" rx="1"/><path d="M3 8h14M7 2v4M13 2v4M6 11h3M11 11h3M6 14h3"/></svg></div>
  <a class="btn btn-orange" style="left:520px;top:1951px;width:160px">View products</a>
</section>

<section>
  <h2 class="title-rule abs" style="left:0;top:2090px;width:1200px"><span class="rule"></span>WHO IS KOVIL FOR?<span class="rule r"></span></h2>
  <div class="aud-circle abs" style="left:135px">
    <svg width="60" height="62" viewBox="0 0 60 62" fill="none" stroke="#123e7c" stroke-width="2.4"><circle cx="14" cy="8" r="4"/><circle cx="30" cy="8" r="4"/><circle cx="46" cy="8" r="4"/><path d="M6 20a8 8 0 0 1 16 0M22 20a8 8 0 0 1 16 0M38 20a8 8 0 0 1 16 0"/><path d="M4 24h52L36 50H24z"/><path d="M34 32c-2-2-8-2-8 1s8 2 8 6-7 3-9 1M30 29v16"/></svg>
    <span class="stem"></span>SALES MANAGERS
  </div>
  <div class="aud-circle abs" style="left:378px">
    <svg width="62" height="62" viewBox="0 0 62 62" fill="none" stroke="#123e7c" stroke-width="2.4"><path d="M4 28L31 4l27 24"/><path d="M10 24v34h42V24"/><path d="M44 6h6v12"/><circle cx="31" cy="40" r="7"/><path d="M31 27v4M31 49v4M18 40h4M40 40h4M22 31l3 3M37 46l3 3M40 31l-3 3M22 49l3-3"/></svg>
    <span class="stem"></span>REAL ESTATE<br>MANAGERS
  </div>
  <div class="aud-circle abs" style="left:620px">
    <svg width="62" height="62" viewBox="0 0 62 62" fill="none" stroke="#123e7c" stroke-width="2.4"><path d="M20 4h16l-4 10h-8z"/><path d="M24 14C10 24 6 38 8 48c2 8 10 10 20 10h6"/><path d="M32 14c6 4 10 9 12 14"/><path d="M30 30c-2-2-9-2-9 2s9 3 9 8-8 4-10 1M25 26v22"/><path d="M48 32l10 4v8c0 7-5 11-10 13-5-2-10-6-10-13v-8z"/><path d="M43 44l4 4 6-7"/></svg>
    <span class="stem"></span>FINANCIALS
  </div>
  <div class="aud-circle abs" style="left:864px">
    <svg width="60" height="62" viewBox="0 0 60 62" fill="none" stroke="#123e7c" stroke-width="2.4"><circle cx="30" cy="24" r="20"/><circle cx="30" cy="24" r="13"/><circle cx="30" cy="20" r="4"/><path d="M22 31a8 8 0 0 1 16 0"/><path d="M16 38L8 54l8-2 4 7 8-15M44 38l8 16-8-2-4 7-8-15"/></svg>
    <span class="stem"></span>BI SPECIALISTS
  </div>
</section>

<section>
  <div class="community-media abs" role="img" aria-label="Group of people stacking hands together in unity, fading into a warm network pattern"></div>
  <h2 class="community-title heading abs">KOVIL &amp; THE COMMUNITY</h2>
  <div class="community-copy abs">
    <p>KOVIL is a secure, integrated data platform designed to bring people, services, and information together—helping communities thrive.</p>
    <p>By bridging the gap between healthcare providers, housing associations, and local support services, KOVIL enables a more joined-up approach to care and wellbeing.</p>
  </div>
  <a class="btn btn-orange" style="left:689px;top:2701px;width:194px">Join the community</a>
</section>

<section>
  <div class="clients-bg abs"></div>
  <h2 class="title-rule abs" style="left:0;top:2877px;width:1200px"><span class="rule"></span>WHAT OUR CLIENTS SAYS<span class="rule r"></span></h2>
  <div class="arrow-btn abs" style="left:134px"><svg width="10" height="10" viewBox="0 0 10 10" fill="none" stroke="#29a9bd" stroke-width="1.6"><path d="M6.5 1.5L3 5l3.5 3.5"/></svg></div>
  <div class="arrow-btn abs" style="left:1034px"><svg width="10" height="10" viewBox="0 0 10 10" fill="none" stroke="#29a9bd" stroke-width="1.6"><path d="M3.5 1.5L7 5 3.5 8.5"/></svg></div>
  <article class="quote-card abs" style="left:185px">
    <span class="quote-mark">“</span>
    <div class="quote-head">
      <div class="avatar" role="img" aria-label="Client portrait"></div>
      <div><div class="quote-name">MARA VELDEN</div>
        <div class="stars">
          <svg width="84" height="15" viewBox="0 0 84 15" fill="#f5b400"><g id="star"><path d="M7.5 0l2.2 4.8 5.2.6-3.9 3.5 1.1 5.1-4.6-2.7-4.6 2.7L4 8.9.1 5.4l5.2-.6z"/></g><use href="#star" x="17"/><use href="#star" x="34"/><use href="#star" x="51"/><use href="#star" x="68"/></svg>
        </div></div>
    </div>
    <p class="quote-text">Lorem ipsum dolor sit amet, consectetur adipiscing elit. Mauris blandit orci elit, eu fringilla ipsum viverra ultrices. Donec aliquet blandit tellus id lacinia. Duis ac sem sed ligula pulvinar rutrum id sed mi. Nunc elit lectus, bibendum non tincidunt sit amet, commodo sit amet felis.</p>
  </article>
  <article class="quote-card abs" style="left:609px">
    <span class="quote-mark">“</span>
    <div class="quote-head">
      <div class="avatar" role="img" aria-label="Client portrait"></div>
      <div><div class="quote-name">MARA VELDEN</div>
        <div class="stars">
          <svg width="84" height="15" viewBox="0 0 84 15" fill="#f5b400"><use href="#star"/><use href="#star" x="17"/><use href="#star" x="34"/><use href="#star" x="51"/><use href="#star" x="68"/></svg>
        </div></div>
    </div>
    <p class="quote-text">Lorem ipsum dolor sit amet, consectetur adipiscing elit. Mauris blandit orci elit, eu fringilla ipsum viverra ultrices. Donec aliquet blandit tellus id lacinia. Duis ac sem sed ligula pulvinar rutrum id sed mi. Nunc elit lectus, bibendum non tincidunt sit amet, commodo sit amet felis.</p>
  </article>
</section>

<section>
  <div class="cta abs"></div>
  <h2 class="title-rule cta-title abs"><span class="rule"></span>READY TO SEE KOVIL IN ACTION?<span class="rule r"></span></h2>
  <p class="cta-sub abs">Join the organisations using KOVIL to improve lives and transform services..</p>
  <a class="btn btn-orange" style="left:459px;top:3396px;width:137px">Plan a demo</a>
  <a class="btn btn-white" style="left:604px;top:3396px;width:137px">Start KOVIL</a>
</section>

<footer class="site-footer abs">
  <div class="brand abs" style="left:122px;top:46px;color:#fff">KOVIL</div>
  <div class="abs" style="left:122px;top:98px;width:26px;height:26px;border-radius:50%;border:1.5px solid #fff"></div>
  <p class="foot-small abs" style="left:122px;top:135px;width:250px">Copyright 2025 KOVIL Data Platform All Rights Reserved.<br>(Disclaimer, Privacy, Terms)</p>
  <div class="foot-col abs" style="left:403px;top:44px;width:230px">
    <h4>ABOUT US</h4>
    <p class="foot-small">KOVIL is a data analytics platform for the healthcare sector and social housing sector. It helps organizations unlock, analyze, and use data to make smarter decisions. KOVIL combines a scalable platform with intelligent tools, a professional community, and BI-as-a-Service.</p>
  </div>
  <div class="foot-col abs" style="left:689px;top:44px;width:210px">
    <h4>CONTACT US</h4>
    <div class="contact-row"><span class="ic"><svg width="12" height="14" viewBox="0 0 12 14" fill="none" stroke="#fff" stroke-width="1.4"><path d="M6 13S1 8 1 5a5 5 0 0 1 10 0c0 3-5 8-5 8z"/><circle cx="6" cy="5" r="1.8"/></svg></span>42 Harbour Lane, Eastfield</div>
    <div class="contact-row"><span class="ic"><svg width="12" height="12" viewBox="0 0 12 12" fill="#fff"><path d="M2.5 1l2 2.5-1.2 1.3a7 7 0 0 0 3.9 3.9L8.5 7.5 11 9.5 9.8 11C5 11 1 7 1 2.2z"/></svg></span>+00 12 345 6789</div>
    <div class="contact-row"><span class="ic"><svg width="12" height="10" viewBox="0 0 12 10" fill="none" stroke="#fff" stroke-width="1.3"><rect x="1" y="1" width="10" height="8"/><path d="M1 1l5 4 5-4"/></svg></span>hello@kovildata.com</div>
  </div>
  <div class="foot-col abs" style="left:944px;top:44px;width:150px">
    <h4>MAIN LINK</h4>
    <div class="foot-links">What is KOVIL?<br>Products<br>Who it's for<br>Community<br>About us<br>Contact</div>
  </div>
</footer>
<div class="foot-divider abs" style="left:376px"></div>
<div class="foot-divider abs" style="left:657px"></div>
<div class="foot-divider abs" style="left:914px"></div>

</body>
</html>
```